The Coral Clinic PowerPoint Design

We are looking for a new PowerPoint template design to reflect our branding and to be used for presentations at international conferences and online conferences. An example of our current template which is outdated is attached. We would like to still have a blue colour background as this represents water (but the exact background can be modified). We would like a professional, modern, and sharp feel to the templates. The template should include an Intro Slide, content slide, and closing/questions slide. The template needs to be prepared for both the standards, the 4:3 and Wide screen 16:9. Logos and branding in the attached power point can be used. Please visit our website www.thecoralclinic.example to see more about the company.

```html
<!DOCTYPE html>
<html lang="en">
<head>
<meta charset="utf-8">
<title>The Coral Clinic – Presentation Template</title>
<link rel="stylesheet" href="https://fonts.googleapis.com/css2?family=Open+Sans:wght@300;400;600;700&display=swap">
<style>
:root{
  --page:#ffffff;
  --navy:#0c1f66;
  --navy-deep:#0a1a58;
  --blue:#2f6cb8;
  --blue-mid:#3b7fc4;
  --blue-light:#7fa6d6;
  --blue-pale:#c8d9ee;
  --cyan:#2aa3d8;
  --cyan-light:#86c9ea;
  --slate:#8fa9cf;
  --white:#ffffff;
  --muted:#6f83b8;
  --badge:#5aa52c;
}
*{margin:0;padding:0;box-sizing:border-box}
html,body{width:900px;height:1200px;overflow:hidden;background:var(--page)}
body{position:relative;font-family:"Open Sans",Arial,sans-serif;color:var(--white)}
.slide{position:absolute;width:238px;height:179px;background:var(--navy);overflow:hidden;box-shadow:4px 5px 12px rgba(0,0,0,.22)}
.abs{position:absolute}
.title{position:absolute;left:20px;top:19px;font-weight:300;font-size:9.5px;letter-spacing:.2px;text-transform:uppercase}
.subtitle{position:absolute;left:20px;top:33px;font-size:2.2px;color:var(--muted);text-transform:uppercase;letter-spacing:.1px}
.brand{position:absolute;right:18px;top:22px;display:flex;align-items:center;gap:2px;font-weight:700;font-size:4.6px;color:var(--white)}
.brand-dot{width:3px;height:3px;border-radius:50%;background:var(--cyan)}
.footer{position:absolute;left:17px;right:17px;bottom:4px;display:flex;justify-content:space-between;font-size:3px;color:var(--muted)}
.footer b{font-weight:400;color:#90a6d8}
.photo{position:absolute}
.box{position:absolute;padding:4px;font-size:2.4px;line-height:1.45}
.box h4{font-weight:400;font-size:3.6px;margin-bottom:2px}
.box .rule{width:6px;height:.4px;background:var(--white);margin:2px 0 3px}
.pattern{position:absolute;background:repeating-linear-gradient(45deg,#0e2470 0 1px,#0a1c5c 1px 2px)}
.sea{background:linear-gradient(180deg,#3aa6d8,#0d4f98)}
.deep{background:linear-gradient(180deg,#2b8fcf,#073d7c)}
.reef{background:linear-gradient(135deg,#6b3a3a,#c9442f 55%,#7b6b4a)}
.fish{background:linear-gradient(135deg,#9bb0c8,#3646b8 55%,#d8d8d0)}
.sand{background:linear-gradient(160deg,#9fb6c6,#e3e6e8)}
.weed{background:linear-gradient(180deg,#5b6b8a,#3b6e3a 60%,#a47a3a)}
.turtle{background:linear-gradient(160deg,#2f8fbf,#6c7f3a 60%,#1f5f9c)}
.people{background:linear-gradient(160deg,#3d5f86,#1e2f4a)}
.gold{background:linear-gradient(160deg,#c99a3c,#7a5a2a 60%,#b7c2c6)}
.jelly{background:linear-gradient(180deg,#f09a3a,#c64a1a 50%,#1242c0)}
.amber{background:radial-gradient(circle at 55% 55%,#ffb84a,#a3410e 40%,#2a1208 70%,#d9d6d2)}
.penguin{background:linear-gradient(180deg,#3ab7c8,#c2d24a 60%,#1f6d80)}
</style>
</head>
<body>

<!-- Slide 1: Intro -->
<section class="slide" style="left:158px;top:12px">
  <div class="brand" style="top:7px;right:14px"><span>The Coral Clinic</span><span class="brand-dot"></span></div>
  <div class="photo fish" style="left:0;top:22px;width:238px;height:88px" role="img" aria-label="Photo of a clown triggerfish in an aquarium"></div>
  <div class="abs" style="left:195px;top:104px;width:40px;height:13px;background:var(--badge)"></div>
  <h1 class="abs" style="left:0;right:0;top:125px;text-align:center;font-weight:400;font-size:7.6px">Module One - Fish Anatomy and Physiology</h1>
  <p class="abs" style="left:0;right:0;top:141px;text-align:center;font-size:3px">Dr Sam Harlow</p>
  <p class="abs" style="left:24px;right:24px;top:152px;text-align:center;font-size:2.5px;line-height:1.4">Examines teleost anatomy in its wide forms as well as practical physiology. To understand how fish survive in an aquatic environment is critical to maintaining their health and wellbeing. Normal anatomy is critical for diagnostics and post-mortems</p>
  <div class="footer"><span>The Coral Clinic presentation to: <b>Harbourside Marine Centre</b></span><span>Page: 1</span></div>
</section>

<!-- Slide 2: Our Team -->
<section class="slide" style="left:518px;top:12px">
  <h2 class="title">Our Team</h2>
  <p class="subtitle">Key notes on this topic and how it fits the wider programme</p>
  <div class="brand"><span>The Coral Clinic</span><span class="brand-dot"></span></div>
  <div class="photo people" style="left:18px;top:52px;width:36px;height:48px" role="img" aria-label="Portrait of a team member in a wetsuit"></div>
  <div class="box" style="left:54px;top:52px;width:65px;height:48px;background:var(--blue)"><h4>Dr Sam Harlow</h4><p>B.V.Sc, MANZCVS, Aquatic Animal Health</p><p style="margin-top:2px">Short profile of this team member, their training and the work they lead.</p></div>
  <div class="photo people" style="left:119px;top:52px;width:36px;height:48px" role="img" aria-label="Portrait of a team member with a sea turtle"></div>
  <div class="box" style="left:155px;top:52px;width:65px;height:48px;background:var(--blue)"><h4>Dr Owen Castell</h4><p>Bachelor of Science in marine biology</p><p style="margin-top:2px">Short profile of this team member, their training and the work they lead.</p></div>
  <div class="box" style="left:18px;top:104px;width:65px;height:48px;background:var(--blue-light)"><h4>Dr Ivan Marsh</h4><p>Marine Biology degree, doctoral research</p><p style="margin-top:2px">Short profile of this team member, their training and the work they lead.</p></div>
  <div class="photo people" style="left:83px;top:104px;width:36px;height:48px" role="img" aria-label="Portrait of a team member outdoors"></div>
  <div class="box" style="left:119px;top:104px;width:65px;height:48px;background:var(--cyan-light)"><h4>Dr. Leo Farren</h4><p>Veterinary science, first class honours</p><p style="margin-top:2px">Short profile of this team member, their training and the work they lead.</p></div>
  <div class="photo people" style="left:184px;top:104px;width:36px;height:48px" role="img" aria-label="Portrait of a team member with a dog"></div>
  <div class="footer"><span>The Coral Clinic presentation to: <b>Harbourside Marine Centre</b></span><span>Page: 2</span></div>
</section>

<!-- Slide 3: Our Vision -->
<section class="slide" style="left:155px;top:210px">
  <h2 class="title">Our Vision</h2>
  <p class="subtitle">Advancing the welfare of aquatic animals in care worldwide</p>
  <div class="brand"><span>The Coral Clinic</span><span class="brand-dot"></span></div>
  <div class="photo penguin" style="left:24px;top:52px;width:38px;height:49px;border-radius:10px 0 0 0" role="img" aria-label="Photo of a penguin swimming"></div>
  <div class="box" style="left:62px;top:52px;width:53px;height:49px;background:var(--blue);border-radius:0 0 14px 0"><h4>Consultation</h4><p>A brief outline of this service and what it offers to partner aquariums.</p></div>
  <div class="photo gold" style="left:121px;top:52px;width:38px;height:49px;border-radius:10px 0 0 0" role="img" aria-label="Photo of a seahorse"></div>
  <div class="box" style="left:159px;top:52px;width:53px;height:49px;background:var(--blue);border-radius:0 0 14px 0"><h4>Education</h4><p>A brief outline of this service and what it offers to partner aquariums.</p></div>
  <div class="photo fish" style="left:24px;top:107px;width:38px;height:49px;border-radius:10px 0 0 0" role="img" aria-label="Photo of a clown triggerfish"></div>
  <div class="box" style="left:62px;top:107px;width:53px;height:49px;background:var(--blue);border-radius:0 0 14px 0"><h4>Conferences</h4><p>A brief outline of this service and what it offers to partner aquariums.</p></div>
  <div class="photo jelly" style="left:121px;top:107px;width:38px;height:49px;border-radius:10px 0 0 0" role="img" aria-label="Photo of an orange jellyfish"></div>
  <div class="box" style="left:159px;top:107px;width:53px;height:49px;background:var(--blue);border-radius:0 0 14px 0"><h4>Reproduction</h4><p>A brief outline of this service and what it offers to partner aquariums.</p></div>
  <div class="footer"><span>The Coral Clinic presentation to: <b>Harbourside Marine Centre</b></span><span>Page: 3</span></div>
</section>

<!-- Slide 4: Content -->
<section class="slide" style="left:518px;top:210px">
  <h2 class="title">Content Slide</h2>
  <p class="subtitle">Key notes on this topic and how it fits the wider programme</p>
  <div class="brand"><span>The Coral Clinic</span><span class="brand-dot"></span></div>
  <div class="footer"><span>The Coral Clinic presentation to: <b>Harbourside Marine Centre</b></span><span>Page: 4</span></div>
</section>

<!-- Slide 5: Text with image -->
<section class="slide" style="left:158px;top:408px">
  <h2 class="title" style="top:37px">Text with Image</h2>
  <p class="subtitle" style="top:52px;width:90px">Key notes on this topic and how it fits the wider programme</p>
  <div class="abs" style="left:18px;top:68px;width:100px;font-size:2.4px;line-height:1.7">
    <p><b>Lorem ipsum</b> opening paragraph that frames the topic for the audience, sets out the main idea and explains why it matters to animal care and to daily practice in the aquarium.</p>
    <p style="margin-top:3px">A second paragraph adds supporting detail, a short example from the field and a closing note that leads the audience into the next part of the talk.</p>
  </div>
  <div class="photo amber" style="left:133px;top:0;width:105px;height:179px" role="img" aria-label="Photo of hands holding a backlit shark egg case"></div>
  <div class="footer" style="right:110px"><span>The Coral Clinic presentation to: <b>Harbourside Marine Centre</b></span></div>
</section>

<!-- Slide 6: Portfolio options -->
<section class="slide" style="left:518px;top:408px">
  <h2 class="title">Portafolio Options</h2>
  <p class="subtitle">Key notes on this topic and how it fits the wider programme</p>
  <div class="brand"><span>The Coral Clinic</span><span class="brand-dot"></span></div>
  <div class="photo turtle" style="left:19px;top:48px;width:55px;height:104px" role="img" aria-label="Photo of a sea turtle among fish"></div>
  <div class="photo deep" style="left:75px;top:48px;width:54px;height:55px" role="img" aria-label="Photo of a shark in blue water"></div>
  <div class="box" style="left:75px;top:104px;width:54px;height:48px;background:var(--blue)"><h4>Content Text here</h4><div class="rule"></div><p><b>Lorem ipsum</b> short note on this image, the species and the topic it shows.</p></div>
  <div class="photo sea" style="left:130px;top:48px;width:90px;height:55px" role="img" aria-label="Photo of an eagle ray swimming"></div>
  <div class="photo sand" style="left:130px;top:104px;width:90px;height:48px" role="img" aria-label="Close-up photo of a shark"></div>
  <div class="footer"><span>The Coral Clinic presentation to: <b>Harbourside Marine Centre</b></span><span>Page: 5</span></div>
</section>

<!-- Slide 7: Portfolio options grid -->
<section class="slide" style="left:158px;top:607px">
  <h2 class="title">Portafolio Options</h2>
  <p class="subtitle">Key notes on this topic and how it fits the wider programme</p>
  <div class="brand"><span>The Coral Clinic</span><span class="brand-dot"></span></div>
  <div class="photo fish" style="left:0;top:52px;width:40px;height:53px" role="img" aria-label="Photo of a clown triggerfish"></div>
  <div class="box" style="left:40px;top:52px;width:39px;height:53px;background:var(--blue)"><h4>Content Text</h4><div class="rule"></div><p><b>Lorem ipsum</b> short note on this image and topic.</p></div>
  <div class="photo weed" style="left:79px;top:52px;width:40px;height:53px" role="img" aria-label="Photo of fish among aquarium plants"></div>
  <div class="box" style="left:119px;top:52px;width:40px;height:53px;background:var(--blue-pale)"><h4>Content Text</h4><div class="rule"></div><p><b>Lorem ipsum</b> short note on this image and topic.</p></div>
  <div class="photo deep" style="left:159px;top:52px;width:40px;height:53px" role="img" aria-label="Photo of a shark"></div>
  <div class="box" style="left:199px;top:52px;width:39px;height:53px;background:var(--cyan)"><h4>Content Text</h4><div class="rule"></div><p><b>Lorem ipsum</b> short note on this image and topic.</p></div>
  <div class="box" style="left:0;top:105px;width:40px;height:52px;background:var(--blue)"><h4>Content Text</h4><div class="rule"></div><p><b>Lorem ipsum</b> short note on this image and topic.</p></div>
  <div class="pattern" style="left:40px;top:105px;width:39px;height:52px"></div>
  <div class="box" style="left:79px;top:105px;width:40px;height:52px;background:var(--slate)"><h4>Content Text</h4><div class="rule"></div><p><b>Lorem ipsum</b> short note on this image and topic.</p></div>
  <div class="pattern" style="left:119px;top:105px;width:40px;height:52px"></div>
  <div class="box" style="left:159px;top:105px;width:40px;height:52px;background:var(--cyan-light)"><h4>Content Text</h4><div class="rule"></div><p><b>Lorem ipsum</b> short note on this image and topic.</p></div>
  <div class="pattern" style="left:199px;top:105px;width:39px;height:52px"></div>
  <div class="footer"><span>The Coral Clinic presentation to: <b>Harbourside Marine Centre</b></span><span>Page: 7</span></div>
</section>

<!-- Slide 8: Portfolio options large image -->
<section class="slide" style="left:517px;top:607px">
  <h2 class="title">Portafolio Options</h2>
  <p class="subtitle">Key notes on this topic and how it fits the wider programme</p>
  <div class="brand"><span>The Coral Clinic</span><span class="brand-dot"></span></div>
  <div class="photo deep" style="left:0;top:52px;width:119px;height:105px" role="img" aria-label="Photo of a large shark in a tank"></div>
  <div class="box" style="left:119px;top:52px;width:40px;height:53px;background:var(--blue-pale)"><h4>Text</h4><div class="rule"></div><p><b>Lorem ipsum</b> short note on this image and topic.</p></div>
  <div class="photo sand" style="left:159px;top:52px;width:40px;height:53px" role="img" aria-label="Close-up photo of a shark"></div>
  <div class="box" style="left:199px;top:52px;width:39px;height:53px;background:var(--cyan)"><h4>Text</h4><div class="rule"></div><p><b>Lorem ipsum</b> short note on this image and topic.</p></div>
  <div class="photo sea" style="left:119px;top:105px;width:40px;height:52px" role="img" aria-label="Photo of an eagle ray"></div>
  <div class="box" style="left:159px;top:105px;width:40px;height:52px;background:var(--cyan-light)"><h4>Text</h4><div class="rule"></div><p><b>Lorem ipsum</b> short note on this image and topic.</p></div>
  <div class="photo reef" style="left:199px;top:105px;width:39px;height:52px" role="img" aria-label="Photo of a red frogfish"></div>
  <div class="footer"><span>The Coral Clinic presentation to: <b>Harbourside Marine Centre</b></span><span>Page: 8</span></div>
</section>

<!-- Slide 9: Text with two images -->
<section class="slide" style="left:155px;top:805px">
  <h2 class="title">Text with Two Images</h2>
  <p class="subtitle">Key notes on this topic and how it fits the wider programme</p>
  <div class="brand"><span>The Coral Clinic</span><span class="brand-dot"></span></div>
  <div class="photo deep" style="left:18px;top:47px;width:97px;height:85px" role="img" aria-label="Photo of a shark in blue water"></div>
  <div class="photo sand" style="left:123px;top:47px;width:97px;height:85px" role="img" aria-label="Close-up photo of a shark"></div>
  <p class="abs" style="left:18px;top:137px;width:97px;font-size:2.4px;line-height:1.5"><b>Lorem ipsum</b> short caption for this image that explains what it shows and why it matters to the talk.</p>
  <p class="abs" style="left:123px;top:137px;width:97px;font-size:2.4px;line-height:1.5"><b>Lorem ipsum</b> short caption for this image that explains what it shows and why it matters to the talk.</p>
  <div class="footer"><span>The Coral Clinic presentation to: <b>Harbourside Marine Centre</b></span><span>Page: 9</span></div>
</section>

<!-- Slide 10: Portfolio images -->
<section class="slide" style="left:517px;top:805px">
  <h2 class="title">Portafolio Images</h2>
  <p class="subtitle">Key notes on this topic and how it fits the wider programme</p>
  <div class="brand"><span>The Coral Clinic</span><span class="brand-dot"></span></div>
  <div class="photo fish" style="left:18px;top:48px;width:91px;height:54px" role="img" aria-label="Photo of a clown triggerfish"></div>
  <div class="photo weed" style="left:110px;top:48px;width:54px;height:54px" role="img" aria-label="Photo of fish among aquarium plants"></div>
  <div class="photo sea" style="left:165px;top:48px;width:55px;height:54px" role="img" aria-label="Photo of an eagle ray"></div>
  <div class="photo reef" style="left:18px;top:103px;width:52px;height:49px" role="img" aria-label="Photo of a red frogfish"></div>
  <div class="photo turtle" style="left:71px;top:103px;width:93px;height:49px" role="img" aria-label="Photo of a sea turtle over a reef"></div>
  <div class="photo turtle" style="left:165px;top:103px;width:55px;height:49px" role="img" aria-label="Close-up photo of a sea turtle"></div>
  <div class="footer"><span>The Coral Clinic presentation to: <b>Harbourside Marine Centre</b></span><span>Page: 10</span></div>
</section>

<!-- Slide 11: Text with four images -->
<section class="slide" style="left:155px;top:1003px">
  <div class="brand" style="left:20px;right:auto;top:23px"><span>The Coral Clinic</span><span class="brand-dot"></span></div>
  <h2 class="abs" style="left:19px;top:59px;font-weight:400;font-size:11px;line-height:.95;text-transform:uppercase">Text Wit<br>Four<br>Images</h2>
  <p class="abs" style="left:20px;top:98px;width:78px;font-size:2.4px;line-height:1.6"><b>Lorem ipsum</b> short text that introduces these images, names the species shown and explains the point they make for this part of the presentation.</p>
  <div class="photo penguin" style="left:106px;top:22px;width:49px;height:100px" role="img" aria-label="Photo of a penguin swimming"></div>
  <div class="photo turtle" style="left:156px;top:22px;width:49px;height:44px" role="img" aria-label="Photo of a sea turtle"></div>
  <div class="photo sea" style="left:156px;top:68px;width:49px;height:89px" role="img" aria-label="Photo of a reef with schooling fish"></div>
  <div class="photo fish" style="left:106px;top:124px;width:49px;height:33px" role="img" aria-label="Photo of a clown triggerfish"></div>
  <div class="abs" style="left:205px;top:67px;width:29px;height:.5px;background:var(--blue-mid)"></div>
  <div class="abs" style="left:0;top:123px;width:106px;height:.5px;background:var(--blue-mid)"></div>
  <div class="footer"><span>The Coral Clinic presentation to: <b>Harbourside Marine Centre</b></span><span>Page: 11</span></div>
</section>

<!-- Slide 12: Questions -->
<section class="slide" style="left:517px;top:1003px">
  <svg class="abs" style="left:0;top:0" width="238" height="179" viewBox="0 0 238 179" aria-hidden="true">
    <polygon points="137,46 146,46 103,152 94,152" fill="#2a8fd0"/>
    <polygon points="150,10 160,10 110,140 100,140" fill="#1f7ac4"/>
    <polygon points="162,8 170,8 118,150 110,150" fill="#3fa3dc"/>
    <polygon points="176,0 186,0 128,162 118,162" fill="#2b7fc6"/>
    <polygon points="190,0 200,0 138,166 128,166" fill="#4db0e2"/>
    <polygon points="213,0 228,0 143,150 128,150" fill="#3d74bf"/>
    <polygon points="178,82 186,82 155,160 147,160" fill="#5a8ed0"/>
  </svg>
  <div class="brand" style="left:20px;right:auto;top:23px"><span>The Coral Clinic</span><span class="brand-dot"></span></div>
  <h2 class="abs" style="left:17px;top:63px;font-weight:400;font-size:15px">QUESTIONS?</h2>
  <p class="abs" style="left:17px;top:84px;width:95px;font-size:2.4px;line-height:1.5">Thank you for listening. We welcome your questions and thoughts on today's topic and our work.</p>
</section>

</body>
</html>
```